Email signature

I have an email signature, card and letter head and I would like the colours darker and more distinctive and I would like the contact details to be bigger and or easier to read as they are hard to read at the moment. The arrow watermark is fine I think.

Logo Text

VANTORA GUARD PTY LTD

Requirements
Nice to have
• The yellow type colour with the grey is good and I would like to retain that, but it looks washed out and too light on the screen. I like the arrows and I like the watermark arrows as well and I would like to retain the basic design.

```html
<!DOCTYPE html>
<html lang="en">
<head>
<meta charset="utf-8">
<title>Vantora Guard – Email Signature</title>
<link rel="stylesheet" href="https://fonts.googleapis.com/css2?family=Roboto:wght@300;400&display=swap">
<style>
  :root {
    --brand-yellow: #e8b400;
    --brand-grey: #3f3f42;
    --watermark-tone: #ececec;
    --paper: #ffffff;
  }
  html, body {
    margin: 0;
    padding: 0;
    overflow: hidden;
    background: var(--paper);
  }
  .signature {
    position: relative;
    width: 1200px;
    height: 681px;
    overflow: hidden;
    background: var(--paper);
    font-family: "Roboto", sans-serif;
    font-weight: 300;
    line-height: 1;
    color: var(--brand-grey);
  }
  .signature > * {
    position: absolute;
    margin: 0;
    white-space: nowrap;
  }
  .watermark {
    left: 0;
    top: 405px;
    width: 680px;
    height: 276px;
    background: linear-gradient(90deg, var(--watermark-tone) 0%, #f5f5f5 55%, rgba(255,255,255,0) 100%);
    opacity: 0.8;
  }
  .brand-mark {
    top: 6px;
    right: 6px;
    width: 62px;
    height: 62px;
    background: var(--brand-yellow);
  }
  .company-name {
    top: -6px;
    right: 92px;
    font-size: 96px;
    font-weight: 300;
    letter-spacing: 1px;
    color: var(--brand-grey);
  }
  .company-suffix {
    top: 91px;
    right: 2px;
    font-size: 70px;
    letter-spacing: 6px;
    color: var(--brand-grey);
  }
  .person-name {
    top: 262px;
    right: 0;
    font-size: 63px;
    letter-spacing: 4px;
  }
  .person-role {
    top: 340px;
    right: 0;
    font-size: 56px;
    letter-spacing: 1px;
    color: var(--brand-yellow);
  }
  .contact-phone {
    top: 478px;
    right: 0;
    font-size: 50px;
    font-weight: 400;
    letter-spacing: 4px;
  }
  .contact-online {
    top: 562px;
    left: 36px;
    right: 2px;
    font-size: 41px;
    font-weight: 400;
    display: flex;
    align-items: baseline;
  }
  .contact-label {
    color: var(--brand-yellow);
  }
  .contact-phone .contact-label {
    margin-right: 26px;
  }
  .contact-online .contact-label {
    margin-right: 28px;
  }
  .contact-email {
    margin-right: 40px;
  }
  .contact-web {
    margin-left: auto;
  }
</style>
</head>
<body>
  <section class="signature" aria-label="Vantora Guard email signature">
    <div class="watermark" role="img" aria-label="Faint chevron arrow watermark"></div>

    <h1 class="company-name">VANTORA GUARD</h1>
    <span class="brand-mark" aria-hidden="true"></span>
    <p class="company-suffix">PTY LTD</p>

    <p class="person-name">DALE MORGAN</p>
    <p class="person-role">DIRECTOR</p>

    <p class="contact-phone"><span class="contact-label">PH</span>0400 555 219</p>

    <p class="contact-online">
      <span class="contact-label">E</span>
      <span class="contact-email">dale@vantoraguard.net.au</span>
      <span class="contact-label">W</span>
      <span class="contact-web">www.vantoraguard.net.au</span>
    </p>
  </section>
</body>
</html>
```